Diagram of Marrowfen’s history for website

This project is to design the attached diagram along the lines of the attached image but in our branding - style guide attached. The diagram will be going on the Marrowfen website - www.marrowfen.au.

```html
<!DOCTYPE html>
<html lang="en">
<head>
<meta charset="utf-8">
<title>Marrowfen’s History</title>
<link rel="stylesheet" href="https://fonts.googleapis.com/css2?family=Poppins:wght@400;600;700&display=swap">
<style>
  :root{
    --ink:#4f4f4f;
    --sand:#d9b19b;
    --sage:#6f9176;
    --mist:#7fa0a6;
    --clay:#a98a7c;
    --forest:#587259;
    --slate:#637a7c;
    --title-green:#587259;
    --title-clay:#ac8b7d;
    --faint:#cdd8d3;
    --paper:#ffffff;
  }
  html,body{margin:0;padding:0;width:1200px;height:1200px;overflow:hidden;background:var(--paper);}
  body{font-family:"Poppins",sans-serif;position:relative;}
  .history{position:absolute;left:0;top:136px;width:1292px;height:1000px;transform:scale(0.9288);transform-origin:0 0;}
  .history-title{position:absolute;left:112px;margin:0;font-weight:700;line-height:1;letter-spacing:-1px;font-size:121px;}
  .history-title .line-one{position:absolute;top:92px;color:var(--title-green);white-space:nowrap;}
  .history-title .line-two{position:absolute;top:200px;color:var(--title-clay);white-space:nowrap;}
  .timeline-graphic{position:absolute;left:0;top:0;width:1292px;height:1000px;}
  .year-label{font-family:"Poppins",sans-serif;font-weight:700;font-size:32px;fill:#fff;}
  .milestone{position:absolute;}
  .milestone h3{margin:0;font-weight:600;font-size:20px;line-height:21px;}
  .milestone p{margin:4px 0 0;font-size:13.4px;line-height:16px;color:var(--ink);}
  .tone-sand h3{color:var(--sand);}
  .tone-sage h3{color:var(--sage);}
  .tone-mist h3{color:var(--mist);}
  .tone-clay h3{color:var(--clay);}
  .tone-forest h3{color:var(--forest);}
  .tone-slate h3{color:var(--slate);}
  .brand-mark{position:absolute;left:392px;top:856px;display:flex;align-items:center;gap:12px;font-weight:600;font-size:34px;color:var(--faint);}
  .brand-mark .dot{width:20px;height:20px;border-radius:50%;background:var(--faint);}
</style>
</head>
<body>
<main class="history">
  <h1 class="history-title"><span class="line-one">MARROWFEN’S</span><span class="line-two">HISTORY</span></h1>

  <svg class="timeline-graphic" viewBox="0 0 1292 1000" aria-hidden="true">
    <g class="connectors" fill="none" stroke-width="1.3">
      <path d="M86 593 V632 H97" stroke="var(--sand)"/>
      <path d="M266 538 V452 H277" stroke="var(--sage)"/>
      <path d="M467 593 V632 H478" stroke="var(--mist)"/>
      <path d="M651 538 V433 H664" stroke="var(--clay)"/>
      <path d="M850 593 V778 H867" stroke="var(--forest)"/>
      <path d="M1030 538 V232 H1041" stroke="var(--slate)"/>
    </g>
    <g class="markers" stroke-width="1.3">
      <g stroke="var(--sand)" fill="#fff"><circle cx="101" cy="632" r="5"/></g>
      <g stroke="var(--sage)" fill="#fff"><circle cx="281" cy="452" r="5"/></g>
      <g stroke="var(--mist)" fill="#fff"><circle cx="482" cy="632" r="5"/></g>
      <g stroke="var(--clay)" fill="#fff"><circle cx="668" cy="433" r="5"/></g>
      <g stroke="var(--forest)" fill="#fff"><circle cx="850" cy="612" r="5"/><circle cx="850" cy="717" r="5"/><circle cx="871" cy="778" r="5"/></g>
      <g stroke="var(--slate)" fill="#fff"><circle cx="1045" cy="232" r="5"/><circle cx="1030" cy="302" r="5"/><circle cx="1030" cy="389" r="5"/><circle cx="1030" cy="467" r="5"/></g>
      <g fill="var(--sand)"><circle cx="101" cy="632" r="2.4"/></g>
      <g fill="var(--sage)"><circle cx="281" cy="452" r="2.4"/></g>
      <g fill="var(--mist)"><circle cx="482" cy="632" r="2.4"/></g>
      <g fill="var(--clay)"><circle cx="668" cy="433" r="2.4"/></g>
      <g fill="var(--forest)"><circle cx="850" cy="612" r="2.4"/><circle cx="850" cy="717" r="2.4"/><circle cx="871" cy="778" r="2.4"/></g>
      <g fill="var(--slate)"><circle cx="1045" cy="232" r="2.4"/><circle cx="1030" cy="302" r="2.4"/><circle cx="1030" cy="389" r="2.4"/><circle cx="1030" cy="467" r="2.4"/></g>
    </g>
    <g class="year-arrows">
      <polygon points="71,538 246,538 265,565.5 246,593 71,593 90,565.5" fill="var(--sand)"/>
      <polygon points="260,538 435,538 454,565.5 435,593 260,593 279,565.5" fill="var(--sage)"/>
      <polygon points="449,538 624,538 643,565.5 624,593 449,593 468,565.5" fill="var(--mist)"/>
      <polygon points="638,538 813,538 832,565.5 813,593 638,593 657,565.5" fill="var(--clay)"/>
      <polygon points="827,538 1002,538 1021,565.5 1002,593 827,593 846,565.5" fill="var(--forest)"/>
      <polygon points="1016,538 1191,538 1210,565.5 1191,593 1016,593 1035,565.5" fill="var(--slate)"/>
    </g>
    <g class="years" text-anchor="middle">
      <text class="year-label" x="167" y="577">2017</text>
      <text class="year-label" x="356" y="577">2018</text>
      <text class="year-label" x="545" y="577">2019</text>
      <text class="year-label" x="735" y="577">2021</text>
      <text class="year-label" x="924" y="577">2022</text>
      <text class="year-label" x="1113" y="577">2023</text>
    </g>
  </svg>

  <section class="milestone tone-sand" style="left:111px;top:602px;width:230px;">
    <h3>Marrowfen<br>Commences</h3>
    <p>Mara started the business with 25 years’ experience working for government &amp; non-government disability &amp; community services. Our first office is in Ferndale &nbsp; NCSS Provider</p>
  </section>

  <section class="milestone tone-sage" style="left:295px;top:440px;width:200px;">
    <h3>Clinic Expansion</h3>
    <p>Marrowfen moves offices twice in Ferndale due to growth &amp; expansion. Clinic established</p>
  </section>

  <section class="milestone tone-mist" style="left:496px;top:601px;width:180px;">
    <h3>Move to<br>Ashbury</h3>
    <p>Marrowfen moves to Ashbury due to further Ashbury due to further growth &amp; expansion</p>
  </section>

  <section class="milestone tone-clay" style="left:682px;top:421px;width:240px;">
    <h3>Purpose-Corporation</h3>
    <p>Marrowfen becomes a accredited Purpose-Corporation having met the highest standards of environmental social &amp; community performance</p>
  </section>

  <section class="milestone tone-forest" style="left:886px;top:600px;width:220px;">
    <h3>Kestrel Best<br>of Business</h3>
    <p>Marrowfen wins the Kestrel Best of Business Award (Vic) for building communities</p>
  </section>

  <section class="milestone tone-forest" style="left:885px;top:705px;width:220px;">
    <h3>Move to Linwood</h3>
    <p>Marrowfen moves to a larger premises in Linwood</p>
  </section>

  <section class="milestone tone-forest" style="left:885px;top:768px;width:230px;">
    <h3>Partnerships</h3>
    <p>Partnerships established with Coral Bay School for Children with Disability &amp; Wirra Centre (Southgate University)</p>
  </section>

  <section class="milestone tone-slate" style="left:1055px;top:205px;width:200px;">
    <h3>Reconciliation<br>Action Plan (RAP)</h3>
    <p>Marrowfen’s Reflect RAP developed &amp; endorsed</p>
  </section>

  <section class="milestone tone-slate" style="left:1055px;top:292px;width:200px;">
    <h3>Client<br>Advisory Group</h3>
    <p>Marrowfen’s Client Advisory Group</p>
  </section>

  <section class="milestone tone-slate" style="left:1054px;top:377px;width:200px;">
    <h3>E-Learning<br>Platform</h3>
    <p>Marrowfen e-learning launched</p>
  </section>

  <section class="milestone tone-slate" style="left:1054px;top:457px;width:200px;">
    <h3>Spectrum Tick</h3>
    <p>Marrowfen achieves Spectrum Tick accreditation</p>
  </section>

  <div class="brand-mark"><span class="dot"></span>Marrowfen</div>
</main>
</body>
</html>
```